Larkspur Ridge Management - Business Cards

I need business cards. My current logo was designed by a designer at this site and I very much like and am happy with the results. I would like a business card that is trendy, unique, current yet professional. I deal with high net worth clients daily

Target Market(s)

Out of state investors looking to get into the rental market in Ohio

Industry/Entity Type

Property Management, Consulting

Contact Information for Business Card

Name, Title (Chief Financial Officer) office phone number (555) 817-3094 website address larkridgemgmt.example

Font styles to use
Sans Serif

Colors
0054AA
0677BA
7BADD7
CADEEF
E8F1F8
0094D4
00A9DD
6FCCEA
C7EBF8
E9F6FB
00AB8E
00BBA5
67D7C9
C6EFE9
E9F9F6

```html
<!DOCTYPE html>
<html lang="en">
<head>
<meta charset="utf-8">
<title>Larkspur Ridge Management – Business Cards</title>
<link href="https://fonts.googleapis.com/css2?family=Poppins:wght@400;600;700&display=swap" rel="stylesheet">
<style>
  :root {
    --backdrop: #98a0a4;
    --card: #ffffff;
    --navy: #1f3461;
    --red: #d8232a;
    --ink: #2b2f38;
    --pattern: #d9dcdf;
  }
  * { margin: 0; padding: 0; box-sizing: border-box; }
  html, body { width: 900px; height: 1200px; overflow: hidden; }
  body {
    background: var(--backdrop);
    font-family: "Poppins", sans-serif;
    position: relative;
  }
  .card {
    position: absolute;
    left: 90px;
    width: 720px;
    height: 411px;
    background: var(--card);
    box-shadow: 0 6px 18px rgba(0,0,0,0.25);
    overflow: hidden;
  }
  .card--front { top: 174px; }
  .card--back { top: 615px; }

  .brand-mark {
    position: absolute;
    display: flex;
    flex-direction: column;
    align-items: center;
    text-align: center;
    color: var(--navy);
    font-weight: 700;
    line-height: 1.1;
    text-transform: uppercase;
  }
  .brand-mark__square {
    background: var(--navy);
    margin-bottom: 14px;
  }
  .card--front .brand-mark {
    left: 38px; top: 120px; width: 230px;
    font-size: 25px;
  }
  .card--front .brand-mark__square { width: 26px; height: 26px; }

  .divider {
    position: absolute;
    left: 290px; top: 50px;
    width: 2px; height: 311px;
    background: linear-gradient(var(--navy), var(--red));
  }
  .contact {
    position: absolute;
    left: 322px; top: 98px;
  }
  .contact__name {
    color: var(--navy);
    font-weight: 700;
    font-size: 34px;
    line-height: 1;
  }
  .contact__title {
    color: var(--ink);
    font-size: 17px;
    margin-top: 6px;
  }
  .contact__list {
    list-style: none;
    margin-top: 34px;
  }
  .contact__item {
    display: flex;
    align-items: center;
    gap: 8px;
    color: var(--ink);
    font-size: 17.5px;
    height: 20px;
    margin-bottom: 20px;
  }
  .contact__icon { width: 16px; height: 16px; fill: var(--red); flex: none; }

  .back-pattern {
    position: absolute; inset: 0;
    background: radial-gradient(circle at 50% 55%, #eceef0 0%, var(--pattern) 70%);
  }
  .card--back .brand-mark {
    left: 160px; top: 130px; width: 400px;
    font-size: 40px;
  }
  .card--back .brand-mark__square { width: 36px; height: 36px; }
</style>
</head>
<body>

<section class="card card--front" aria-label="Business card front">
  <div class="brand-mark">
    <span class="brand-mark__square"></span>
    <span>Larkspur Ridge Management</span>
  </div>
  <div class="divider"></div>
  <div class="contact">
    <h1 class="contact__name">JORDAN AVERY</h1>
    <p class="contact__title">Chief Financial Officer</p>
    <ul class="contact__list">
      <li class="contact__item">
        <svg class="contact__icon" viewBox="0 0 24 24"><path d="M6.6 10.8a15.1 15.1 0 0 0 6.6 6.6l2.2-2.2a1 1 0 0 1 1-.25 11.4 11.4 0 0 0 3.6.57 1 1 0 0 1 1 1V20a1 1 0 0 1-1 1A17 17 0 0 1 3 4a1 1 0 0 1 1-1h3.5a1 1 0 0 1 1 1c0 1.25.2 2.45.57 3.57a1 1 0 0 1-.25 1z"/></svg>
        (555) 817-3094
      </li>
      <li class="contact__item">
        <svg class="contact__icon" viewBox="0 0 24 24"><path d="M2 5h20v14H2z M3 6l9 7 9-7" /><path d="M2 5l10 8 10-8v-.5H2z" fill="#fff" opacity=".9"/></svg>
        info@larkridgemgmt.example
      </li>
      <li class="contact__item">
        <svg class="contact__icon" viewBox="0 0 24 24"><circle cx="12" cy="12" r="10"/><path d="M2 12h20M12 2c3 3 3 17 0 20M12 2c-3 3-3 17 0 20" stroke="#fff" stroke-width="1.4" fill="none"/></svg>
        www.larkridgemgmt.example
      </li>
    </ul>
  </div>
</section>

<section class="card card--back" aria-label="Business card back">
  <div class="back-pattern" role="img" aria-label="Faint repeating brand pattern in light grey"></div>
  <div class="brand-mark">
    <span class="brand-mark__square"></span>
    <span>Larkspur Ridge Management</span>
  </div>
</section>

</body>
</html>
```